Custom beer tap decals, Halvett Brewery, Tasmania, Australia.

UPDATE 22/6/2017

Based on designs received so far, Im after more of a bold/clean design. This must standout. See attached example.

Beer tap decals for 4 different products. Rustic/English feel, with some modern vibrancy, maintain original branding as much as possible.
The size bust be a 95mm circle. Please see attached artwork.
The same branding theme must carry across all four designs. While each can be different, the core branding remaining the same is important.
Happy for different fonts to be used, but they must be clearly readable. The font for the 'Halvett Brewery' component must remain the same.
The colours used in the flag banner part of the decal must remain the same as these reflect the colours on our bottle labels.

Highlighting the 'Made in Tasmania' component would be nice, although not entirely necessary.

Plus a 'Limited Release; design including white space where one off beers can be written in permanent marker, we brew quite a few small batch beers per year and it doesn’t make sense to have custom decals for each. Having a generic limited release decal that we can change ourselves would be a big help.

Target Market(s)

Graphic design, beer, brewery.

Industry/Entity Type

Brewery

Colors

Designer to choose colors to be used in the design.

Requirements
Must have
• 'Halvett Brewery' component of supplied decals must remain. Would be nice to incorporate some of the shield elements, but isn't vital.
Nice to have
• Rustic/earth themes, with a modern twist and vibrance.

```html
<!DOCTYPE html>
<html lang="en">
<head>
<meta charset="utf-8">
<title>Halvett Brewery – Beer Tap Decals</title>
<link rel="stylesheet" href="https://fonts.googleapis.com/css2?family=Alfa+Slab+One&family=Arvo:wght@700&display=swap">
<style>
  :root {
    --bg-centre: #9a0c36;
    --bg-edge: #4a0018;
    --cream: #f3eccb;
    --cream-light: #f8f3da;
    --ink: #1c1a17;
    --white: #ffffff;
    --stout-green: #2a7b3d;
    --red-ale: #b4263c;
    --bitter-gold: #c9a34c;
    --pale-orange: #f08a26;
    --limited-blue: #1f66b6;
    --hop-green: #4f9a34;
  }
  html, body {
    margin: 0;
    padding: 0;
    overflow: hidden;
  }
  body {
    width: 1200px;
    height: 960px;
    background: radial-gradient(ellipse at 50% 55%, var(--bg-centre) 0%, var(--bg-edge) 100%);
  }
  .decal-sheet {
    display: block;
    width: 1200px;
    height: 960px;
  }
  .decal-shadow { fill: rgba(0,0,0,0.35); }
  .rim-outer { fill: var(--cream); }
  .rim-inner { fill: var(--white); }
  .face { fill: var(--cream); }
  .face-line { fill: none; stroke: var(--ink); stroke-width: 2; }
  .hop-placeholder { fill: var(--hop-green); }
  .brand-name {
    font-family: "Arvo", Georgia, serif;
    font-weight: 700;
    font-size: 50px;
    letter-spacing: 1px;
    fill: var(--ink);
    text-anchor: middle;
  }
  .brand-sub {
    font-family: "Arvo", Georgia, serif;
    font-weight: 700;
    font-size: 17px;
    letter-spacing: 2px;
    fill: var(--ink);
    text-anchor: middle;
  }
  .banner-line { stroke: var(--ink); stroke-width: 2; stroke-linejoin: round; }
  .banner-fold { fill: rgba(0,0,0,0.25); }
  .beer-name {
    font-family: "Alfa Slab One", Georgia, serif;
    font-size: 22px;
    letter-spacing: 1px;
    text-anchor: middle;
  }
  .beer-name--dark { fill: var(--ink); }
  .beer-name--light { fill: var(--white); }
  .origin-small {
    font-family: "Arvo", Georgia, serif;
    font-weight: 700;
    font-size: 13px;
    fill: var(--ink);
    text-anchor: middle;
  }
  .origin-large {
    font-family: "Arvo", Georgia, serif;
    font-weight: 700;
    font-size: 18px;
    fill: var(--ink);
    text-anchor: middle;
  }
  .abv {
    font-family: "Arvo", Georgia, serif;
    font-weight: 700;
    font-size: 24px;
    fill: var(--ink);
    text-anchor: middle;
  }
  .limited-plate { fill: var(--ink); }
  .limited-word {
    font-family: "Alfa Slab One", Georgia, serif;
    font-size: 36px;
    fill: var(--limited-blue);
    stroke: var(--white);
    stroke-width: 1.5;
    paint-order: stroke;
    text-anchor: middle;
  }
</style>
</head>
<body>
<svg class="decal-sheet" viewBox="0 0 1200 960" xmlns="http://www.w3.org/2000/svg">
  <defs>
    <symbol id="banner" viewBox="-180 0 360 90" overflow="visible">
      <path class="banner-line" fill="currentColor" d="M-92 34 L-176 40 L-156 58 L-178 80 L-92 74 Z"/>
      <path class="banner-line" fill="currentColor" d="M92 34 L176 40 L156 58 L178 80 L92 74 Z"/>
      <path class="banner-fold" d="M-110 64 L-92 74 L-92 60 Z"/>
      <path class="banner-fold" d="M110 64 L92 74 L92 60 Z"/>
      <path class="banner-line" fill="currentColor" d="M-112 26 Q0 16 112 26 L112 66 Q0 56 -112 66 Z"/>
    </symbol>
    <g id="decal-base">
      <circle class="decal-shadow" cx="3" cy="6" r="182"/>
      <circle class="rim-outer" r="180"/>
      <circle class="rim-band" r="172" fill="currentColor"/>
      <circle class="rim-inner" r="155"/>
      <circle class="face" r="151"/>
      <circle class="face-line" r="140"/>
    </g>
  </defs>

  <!-- Irish Stout -->
  <g class="decal decal--stout" transform="translate(198 310)" style="color: var(--stout-green)">
    <use href="#decal-base"/>
    <ellipse class="hop-placeholder" cx="0" cy="-138" rx="64" ry="40" role="img" aria-label="Hop cone with leaves illustration"/>
    <text class="brand-name" y="-40">HALVETT</text>
    <text class="brand-sub" y="-16">BREWERY</text>
    <use href="#banner" x="-180" y="0" width="360" height="90" style="color: var(--cream-light)"/>
    <text class="beer-name beer-name--dark" y="54">IRISH STOUT</text>
    <text class="origin-small" y="88">PROUDLY</text>
    <text class="origin-large" y="106">TASMANIAN MADE</text>
    <text class="abv" y="134">4.7%</text>
  </g>

  <!-- Irish Red Ale -->
  <g class="decal decal--red-ale" transform="translate(600 310)" style="color: var(--red-ale)">
    <use href="#decal-base"/>
    <ellipse class="hop-placeholder" cx="0" cy="-138" rx="64" ry="40" role="img" aria-label="Hop cone with leaves illustration"/>
    <text class="brand-name" y="-40">HALVETT</text>
    <text class="brand-sub" y="-16">BREWERY</text>
    <use href="#banner" x="-180" y="0" width="360" height="90" style="color: var(--red-ale)"/>
    <text class="beer-name beer-name--light" y="54">IRISH RED ALE</text>
    <text class="origin-small" y="88">PROUDLY</text>
    <text class="origin-large" y="106">TASMANIAN MADE</text>
    <text class="abv" y="134">5.1%</text>
  </g>

  <!-- English Bitter -->
  <g class="decal decal--bitter" transform="translate(1002 310)" style="color: var(--bitter-gold)">
    <use href="#decal-base"/>
    <ellipse class="hop-placeholder" cx="0" cy="-138" rx="64" ry="40" role="img" aria-label="Hop cone with leaves illustration"/>
    <text class="brand-name" y="-40">HALVETT</text>
    <text class="brand-sub" y="-16">BREWERY</text>
    <use href="#banner" x="-180" y="0" width="360" height="90" style="color: var(--bitter-gold)"/>
    <text class="beer-name beer-name--dark" y="54">ENGLISH BITTER</text>
    <text class="origin-small" y="88">PROUDLY</text>
    <text class="origin-large" y="106">TASMANIAN MADE</text>
    <text class="abv" y="134">4.2%</text>
  </g>

  <!-- Pale Ale -->
  <g class="decal decal--pale-ale" transform="translate(398 652)" style="color: var(--pale-orange)">
    <use href="#decal-base"/>
    <ellipse class="hop-placeholder" cx="0" cy="-138" rx="64" ry="40" role="img" aria-label="Hop cone with leaves illustration"/>
    <text class="brand-name" y="-40">HALVETT</text>
    <text class="brand-sub" y="-16">BREWERY</text>
    <use href="#banner" x="-180" y="0" width="360" height="90" style="color: var(--pale-orange)"/>
    <text class="beer-name beer-name--dark" y="54">PALE ALE</text>
    <text class="origin-small" y="88">PROUDLY</text>
    <text class="origin-large" y="106">TASMANIAN MADE</text>
    <text class="abv" y="134">5% ABV</text>
  </g>

  <!-- Limited Release -->
  <g class="decal decal--limited" transform="translate(804 652)" style="color: var(--limited-blue)">
    <use href="#decal-base"/>
    <ellipse class="hop-placeholder" cx="0" cy="-138" rx="64" ry="40" role="img" aria-label="Hop cone with leaves illustration"/>
    <text class="brand-name" y="-46" style="font-size:44px">HALVETT</text>
    <text class="brand-sub" y="-24">BREWERY</text>
    <use href="#banner" x="-180" y="-18" width="360" height="90" style="color: var(--white)"/>
    <rect class="limited-plate" x="-104" y="68" width="208" height="82" rx="6"/>
    <text class="limited-word" y="104">LIMITED</text>
    <text class="limited-word" y="142">RELEASE</text>
  </g>
</svg>
</body>
</html>
```